Animal Eye Clinic needs a Business card

We are a new veterinary ophthalmology practice (Tessaly Animal Eye Care) and we need a business card designed. We only see animal eyes - we are not a regular veterinary clinic. We already have a logo. We are looking for a professional, good looking business card to hand out to our clients. We are looking for something simple but professional and contemporary. Our logo is likely the only picture/graphic that needs to be on the card.
Updates

Contact Information for Business Card

Marisol Dunkley, BSc, DVM, MSc, DipACVO
Veterinary Ophthalmologist

Phone: 250.418.3097
Email: tessalyanimaleyecare@mailbrook.net
Website: tessalyanimaleyecare.net
Address: 1840 Pellworth Rd
Kelowna, BC, V4T 8M3

Colors

Designer to choose colors to be used in the design.

Requirements
Must have
• Our logo (attached)

```html
<!DOCTYPE html>
<html lang="en">
<head>
<meta charset="utf-8">
<title>Tessaly Animal Eye Care – Business Card</title>
<link rel="stylesheet" href="https://fonts.googleapis.com/css2?family=Open+Sans:wght@300;400;600;700&display=swap">
<style>
  :root {
    --teal: #0e9aa9;
    --teal-pale: #e4f3f5;
    --ink: #5a5a5a;
    --grey-block: #8a8a8a;
    --card-black: #1c1c1c;
    --pattern-dark: #141414;
    --pattern-light: #3a3a3a;
    --stage: #3a3a3a;
    --white: #ffffff;
  }
  * { box-sizing: border-box; margin: 0; padding: 0; }
  html, body { width: 1200px; height: 901px; overflow: hidden; }
  body {
    background: var(--stage);
    font-family: "Open Sans", Arial, sans-serif;
    position: relative;
  }
  .card {
    position: absolute;
    left: 250px;
    width: 700px;
    height: 400px;
    overflow: hidden;
  }
  /* Back side */
  .card-back { top: 30px; background: var(--card-black); }
  .back-pattern {
    position: absolute; inset: 0;
    background: linear-gradient(120deg, var(--pattern-dark) 0%, var(--pattern-dark) 45%, var(--pattern-light) 100%);
  }
  .back-brand {
    position: absolute;
    left: 330px; top: 175px;
    display: flex; align-items: center; gap: 14px;
  }
  .brand-dot {
    width: 44px; height: 44px; border-radius: 50%;
    background: var(--teal); flex: none;
  }
  .brand-name {
    color: var(--teal);
    font-weight: 700;
    font-size: 22px;
    letter-spacing: 0.5px;
    text-transform: uppercase;
    line-height: 1;
  }
  /* Front side */
  .card-front { top: 471px; background: var(--white); }
  .front-decoration {
    position: absolute;
    right: 30px; top: 80px;
    width: 230px; height: 230px; border-radius: 50%;
    background: var(--teal-pale);
  }
  .front-brand {
    position: absolute; left: 40px; top: 40px;
    display: flex; align-items: center; gap: 14px;
  }
  .holder {
    position: absolute; left: 40px; top: 118px;
  }
  .holder-name { color: var(--teal); font-weight: 700; font-size: 22px; }
  .holder-creds { color: var(--teal); font-weight: 600; font-size: 14px; }
  .holder-title { color: var(--ink); font-weight: 300; font-size: 20px; margin-top: 2px; }
  .contacts {
    position: absolute; left: 40px; top: 196px;
    list-style: none;
  }
  .contacts li {
    display: flex; align-items: center; gap: 10px;
    color: var(--ink); font-size: 17px; font-weight: 400; line-height: 27px;
  }
  .contacts svg { width: 14px; height: 14px; fill: var(--teal); flex: none; }
  .contacts .web-host { color: var(--teal); }
  .divider {
    position: absolute; left: 40px; top: 292px;
    width: 600px; height: 1px; background: var(--ink);
  }
  .address {
    position: absolute; left: 40px; top: 306px;
    color: var(--ink); font-size: 19px; font-weight: 400;
  }
  .footer-band {
    position: absolute; left: 0; right: 0; bottom: 0; height: 18px;
    display: flex; gap: 10px;
  }
  .footer-grey { width: 50px; background: var(--grey-block); }
  .footer-teal { flex: 1; background: var(--teal); }
</style>
</head>
<body>

<section class="card card-back" aria-label="Card back">
  <div class="back-pattern" role="img" aria-label="Embossed repeating pattern of the clinic's eye-and-animals mark"></div>
  <div class="back-brand">
    <span class="brand-dot"></span>
    <span class="brand-name">Tessaly Animal Eye Care</span>
  </div>
</section>

<section class="card card-front" aria-label="Card front">
  <div class="front-decoration" role="img" aria-label="Large faint clinic mark"></div>

  <div class="front-brand">
    <span class="brand-dot"></span>
    <span class="brand-name">Tessaly Animal Eye Care</span>
  </div>

  <div class="holder">
    <p><span class="holder-name">Marisol Dunkley</span><span class="holder-creds">, BSc, DVM, MSc, DipACVO</span></p>
    <p class="holder-title">Veterinary Ophthalmologist</p>
  </div>

  <ul class="contacts">
    <li>
      <svg viewBox="0 0 24 24" aria-hidden="true"><path d="M6.6 10.8a15.1 15.1 0 0 0 6.6 6.6l2.2-2.2c.3-.3.7-.4 1-.2 1.1.4 2.3.6 3.6.6.6 0 1 .4 1 1V20c0 .6-.4 1-1 1A17 17 0 0 1 3 4c0-.6.4-1 1-1h3.5c.6 0 1 .4 1 1 0 1.3.2 2.5.6 3.6.1.3 0 .7-.2 1z"/></svg>
      250.418.3097
    </li>
    <li>
      <svg viewBox="0 0 24 24" aria-hidden="true"><path d="M2 5h20v14H2z M2 5l10 8 10-8" stroke="#fff" stroke-width="1.5"/></svg>
      tessalyanimaleyecare@mailbrook.net
    </li>
    <li>
      <svg viewBox="0 0 24 24" aria-hidden="true"><circle cx="12" cy="12" r="10"/><path d="M2 12h20M12 2c3 3 3 17 0 20M12 2c-3 3-3 17 0 20" stroke="#fff" stroke-width="1.5" fill="none"/></svg>
      <span>www.<span class="web-host">tessalyanimaleyecare</span>.net</span>
    </li>
  </ul>

  <div class="divider"></div>
  <p class="address">1840 Pellworth Rd, Kelowna, BC, V4T 8M3</p>

  <div class="footer-band">
    <span class="footer-grey"></span>
    <span class="footer-teal"></span>
  </div>
</section>

</body>
</html>
```